Etiketten für Imkerei aus der Steiermark
Zielgruppe
Wir sind eine Imkerei aus der Steiermark / Österreich im Vollerwerb. www.talmann-biene.at
Zielgruppe: Frauen, Familien, Regional
Unser Image: hohe Qualität, Familienbetrieb, naturnah, gesund
Vermarktung: Direkt, Verkaufsstellen, Märkte, zukünftig auch online
Aufgabenstellung
Wir werden die Honiggläser und die Druckerei umstellen und möchten hierfür ein profesionelles abgestimmtes Design. Unser Logo soll erhalten bleiben. Die Honigsortenbezeichnung (Waldhonig, Cremehonig, Blütenhonig) soll zukünftig eingedruckt werden und neben dem Logo ein Zentrales Element sein.
In Zukunft verwenden wir Vintra Gläser mit hohen Deckel der Firma Glasoria in den Größen 1000g(Lise 785), 500g (Vin 410), 250 g (Vin 212) und 150 g (Vin 125). Der Deckel soll einheitlich Gold oder Silber sein.

```html
<!DOCTYPE html>
<html lang="de">
<head>
<meta charset="utf-8">
<title>Honig-Etiketten – talmannbiene</title>
<link href="https://fonts.googleapis.com/css2?family=Amatic+SC:wght@700&family=Mulish:wght@400;800&family=Oswald:wght@300;500&display=swap" rel="stylesheet">
<style>
  :root {
    --bg: #bdbdbd;
    --label: #ffffff;
    --ink: #3f3f3f;
    --ink-soft: #5a5a5a;
    --wald: #9dba3a;
    --bluete: #e08f7a;
    --creme: #e2bb5a;
    --brand-dot: #f5e04a;
  }
  * { margin: 0; padding: 0; box-sizing: border-box; }
  html, body { width: 898px; height: 1200px; overflow: hidden; }
  body { background: var(--bg); position: relative; font-family: "Mulish", sans-serif; color: var(--ink); }

  .label {
    position: absolute;
    width: 415px;
    height: 249px;
    background: var(--label);
  }
  .label--wald   { left: 15px;  top: 303px; --accent: var(--wald); }
  .label--bluete { left: 467px; top: 367px; --accent: var(--bluete); }
  .label--creme  { left: 239px; top: 648px; --accent: var(--creme); }

  .best-before {
    position: absolute;
    right: 14px; top: 15px;
    font-family: "Oswald", sans-serif;
    font-weight: 500;
    font-size: 8px;
    color: var(--ink-soft);
  }
  .variety {
    position: absolute;
    left: 0; right: 0; top: 30px;
    text-align: center;
    font-family: "Amatic SC", cursive;
    font-weight: 700;
    font-size: 46px;
    line-height: 1;
    letter-spacing: 1px;
    color: var(--ink);
  }
  .quality-band {
    position: absolute;
    left: 92px; top: 79px;
    width: 231px; height: 22px;
    background: var(--accent);
    color: #fff;
    font-size: 12px;
    letter-spacing: 1px;
    line-height: 22px;
    text-align: center;
    white-space: nowrap;
  }
  .weight {
    position: absolute;
    left: 0; right: 0; top: 106px;
    text-align: center;
    font-weight: 800;
    font-size: 11px;
  }
  .brand {
    position: absolute;
    left: 0; right: 0; top: 178px;
    display: flex; align-items: center; justify-content: center; gap: 5px;
    font-weight: 800;
    font-size: 14px;
    color: var(--ink);
  }
  .brand-dot { width: 10px; height: 10px; border-radius: 50%; background: var(--brand-dot); }
  .web {
    position: absolute;
    left: 0; right: 0; top: 225px;
    text-align: center;
    font-family: "Oswald", sans-serif;
    font-weight: 500;
    font-size: 9.5px;
    color: var(--ink);
  }
  .address {
    position: absolute;
    left: 14px; top: 178px;
    font-family: "Oswald", sans-serif;
    font-weight: 300;
    font-size: 9.5px;
    line-height: 12px;
    color: var(--ink-soft);
    font-style: normal;
  }
  .storage {
    position: absolute;
    right: 14px; top: 213px;
    text-align: right;
    font-family: "Oswald", sans-serif;
    font-weight: 300;
    font-size: 9.5px;
    line-height: 12px;
    color: var(--ink-soft);
  }
</style>
</head>
<body>

<section class="label label--wald">
  <p class="best-before">Mindesten haltbar bis:</p>
  <h2 class="variety">WALDHONIG</h2>
  <p class="quality-band">Österreichischer Qualitätshonig</p>
  <p class="weight">150g</p>
  <address class="address">Meisterimkerei Talmann<br>Birkengraben 17<br>8124 Lindental<br>Tel: 0664 /31 57 204<br>talmann-biene@mail.at</address>
  <p class="brand"><span class="brand-dot"></span>talmannbiene</p>
  <p class="web">www.talmann-biene.at</p>
  <p class="storage">Trocken und vor Wärme<br>geschützt lagern!</p>
</section>

<section class="label label--bluete">
  <p class="best-before">Mindesten haltbar bis:</p>
  <h2 class="variety">BLÜTENHONIG</h2>
  <p class="quality-band">Österreichischer Qualitätshonig</p>
  <p class="weight">150g</p>
  <address class="address">Meisterimkerei Talmann<br>Birkengraben 17<br>8124 Lindental<br>Tel: 0664 /31 57 204<br>talmann-biene@mail.at</address>
  <p class="brand"><span class="brand-dot"></span>talmannbiene</p>
  <p class="web">www.talmann-biene.at</p>
  <p class="storage">Trocken und vor Wärme<br>geschützt lagern!</p>
</section>

<section class="label label--creme">
  <p class="best-before">Mindesten haltbar bis:</p>
  <h2 class="variety">CREMEHONIG</h2>
  <p class="quality-band">Österreichischer Qualitätshonig</p>
  <p class="weight">150g</p>
  <address class="address">Meisterimkerei Talmann<br>Birkengraben 17<br>8124 Lindental<br>Tel: 0664 /31 57 204<br>talmann-biene@mail.at</address>
  <p class="brand"><span class="brand-dot"></span>talmannbiene</p>
  <p class="web">www.talmann-biene.at</p>
  <p class="storage">Trocken und vor Wärme<br>geschützt lagern!</p>
</section>

</body>
</html>
```